Business cards for Paperleaf Sprites

Please note that the color of the logo has been changed from green to teal blue. Sorry for the changing!

Anything will go but want to have some funky side.

I would like the front of the business card is the logo and business information and the back side is the Adult Coloring, so that would attract the customer to do the coloring on the other side. Have more interactive side. (pictures for references only can see it below). Fairies on the back of the card for coloring and whatever you want to adds on to color, like flowers, nature etc......

Scrapbooking is not just paper, it also involves watercolor, mixed media, art, all the fun stuff.

Another keypoint I would like to stress on is the back of the business card should be Adult Coloring and make sure you are not google and use the search engine to copy and paste because of the copyright issue.

As a designer, I am sure you all can create beautiful artwork.

Please submit your creativities!

Want the business card is out of the ordinary and customers would like to keep that as a keepsake rather than treat like a regular business card and trash it. Fonts cannot be too small, consider some of the customers have to wear bi-focal eyeglasses.

Thanks a lot!

Target Market(s)

Scrapbooking, Card making, papercraft, stampin‘ , gifts items , etc.

Industry/Entity Type

Retail

Contact Information for Business Card

Color Scheme, please match with the Logo. Watercolor effect is nice!
Thanks!

Font styles to use
Serif

Requirements
Must have
• I would like Elegant and playful.
• Thanks!
Nice to have
• Watercolor effect or check out the Adult Coloring Book, I am thinking we can use a double-sided business card, one side for the information and the other side for people can do the coloring. I have attached 2 pictures for reference.
Should not have
• No black color on the background please!

```html
<!DOCTYPE html>
<html lang="en">
<head>
<meta charset="utf-8">
<title>Paperleaf Sprites – Business Card</title>
<link href="https://fonts.googleapis.com/css2?family=Questrial&family=Varela+Round&display=swap" rel="stylesheet">
<style>
  :root {
    --page-bg: #e9e6e2;
    --card-bg: #ffffff;
    --teal: #2fb3a8;
    --teal-light: #9fdcd5;
    --teal-deep: #2f7f8c;
    --frame-grey: #8a8a8a;
    --frame-aqua: #7fe0e3;
    --accent-red: #b2222c;
    --text-grey: #5a5a5a;
    --text-dark: #1f1f1f;
  }
  * { margin: 0; padding: 0; box-sizing: border-box; }
  html, body { width: 1200px; height: 1200px; overflow: hidden; }
  body { background: var(--page-bg); position: relative; font-family: "Questrial", sans-serif; }

  .card {
    position: absolute;
    left: 283px;
    width: 635px;
    height: 402px;
    background: var(--card-bg);
    overflow: hidden;
  }
  .card--front { top: 159px; }
  .card--back { top: 639px; }

  .card__frame {
    position: absolute;
    inset: 17px;
    border: 1px solid var(--frame-grey);
    pointer-events: none;
  }
  .card--back .card__frame { border-color: var(--teal-deep); border-top-color: var(--frame-aqua); }

  .wash { position: absolute; inset: 0; width: 100%; height: 100%; }

  .brand {
    position: absolute;
    left: 157px; width: 320px;
    top: 176px; height: 48px;
    display: flex; align-items: center; justify-content: center; gap: 10px;
  }
  .brand__dot { width: 14px; height: 14px; border-radius: 50%; background: var(--teal-deep); flex: none; }
  .brand__name { font-family: "Questrial", sans-serif; font-size: 32px; line-height: 48px; color: var(--teal-deep); letter-spacing: 0.5px; white-space: nowrap; }

  .details { position: absolute; left: 0; right: 0; top: 0; text-align: center; }
  .details__role { position: absolute; left: 0; right: 0; top: 64px; font-size: 20px; color: var(--accent-red); }
  .details__name { position: absolute; left: 0; right: 0; top: 99px; font-family: "Varela Round", sans-serif; font-size: 36px; font-weight: 700; color: var(--text-grey); letter-spacing: 0.5px; -webkit-text-stroke: 0.8px var(--text-grey); }
  .details__email { position: absolute; left: 0; right: 0; top: 148px; font-size: 12.5px; color: var(--text-dark); letter-spacing: 0.8px; }
  .details__divider { position: absolute; left: 42px; right: 42px; top: 193px; border-top: 2px dotted #b8b8b8; }
  .details__address { position: absolute; left: 0; right: 0; top: 212px; font-size: 16px; line-height: 24px; color: var(--text-dark); letter-spacing: 1.2px; }
  .details__phone { position: absolute; left: 0; right: 0; top: 302px; font-size: 22px; color: var(--accent-red); letter-spacing: 1px; display: flex; justify-content: center; align-items: center; gap: 4px; }
  .details__phone svg { width: 12px; height: 16px; }
  .details__web { position: absolute; left: 0; right: 0; top: 344px; font-size: 12.5px; color: var(--text-dark); letter-spacing: 0.8px; }
</style>
</head>
<body>

<section class="card card--front">
  <svg class="wash" viewBox="0 0 635 402" role="img" aria-label="Teal watercolour brush strokes sweeping diagonally across the card">
    <defs>
      <linearGradient id="washFront" x1="0" y1="1" x2="1" y2="0">
        <stop offset="0" stop-color="var(--teal)"/>
        <stop offset="0.6" stop-color="var(--teal)"/>
        <stop offset="1" stop-color="var(--teal-light)"/>
      </linearGradient>
    </defs>
    <path fill="url(#washFront)" opacity="0.9"
      d="M160 0 L520 0 L560 60 L530 150 L545 230 L500 330 L430 402 L190 402 L130 350 L160 260 L140 200 L180 110 L150 40 Z"/>
    <ellipse cx="317" cy="200" rx="162" ry="108" fill="var(--card-bg)"/>
  </svg>
  <div class="brand">
    <span class="brand__dot"></span>
    <span class="brand__name">Paperleaf Sprites</span>
  </div>
  <div class="card__frame"></div>
</section>

<section class="card card--back">
  <svg class="wash" viewBox="0 0 635 402" role="img" aria-label="Teal watercolour brush strokes in the top right corner">
    <defs>
      <linearGradient id="washBack" x1="0" y1="0" x2="1" y2="0">
        <stop offset="0" stop-color="var(--teal-light)"/>
        <stop offset="1" stop-color="var(--teal)"/>
      </linearGradient>
    </defs>
    <path fill="url(#washBack)" d="M500 0 L635 0 L635 250 L610 300 L600 230 L580 200 L585 150 L560 110 L540 60 Z"/>
  </svg>
  <div class="details">
    <p class="details__role">President</p>
    <h1 class="details__name">Maren Aldous</h1>
    <p class="details__email">hello@paperleafsprites.com</p>
    <div class="details__divider"></div>
    <p class="details__address">Unit 4, 2218-41 Avenue, PO Box 3390<br>Cedar Hollow, Alberta<br>Canada T0E 2K4</p>
    <p class="details__phone">
      <svg viewBox="0 0 12 16" aria-hidden="true"><path fill="var(--accent-red)" d="M8 1 C4 2 2 5 2 8 C2 11 4 14 8 15 L9 12 C7 11 6 10 6 8 C6 6 7 5 9 4 Z"/></svg>
      (780) 555-0142
    </p>
    <p class="details__web">www.paperleafsprites.com</p>
  </div>
  <div class="card__frame"></div>
</section>

</body>
</html>
```